International Educational/Tuition/Learning Center

Company Background:
- Business card for a educational/tuition/learning center that provides supplementary lessons for students in Grade 7 to 12 ( Secondary and JC syllabus in the GCE 'O' and GCE 'A' level context but not limited to these. Future plans will be to cater for SAT, IB and HSCs programs.
- Name of company is called "THE QUILL AND LANTERN".
- Vision is to complement the basic principles of the rote learning culture and value-add by training the students to think out of the box and preserve creativity.
- To re-define and retain the value of the learning process.

Sketch Design:
- Simple and classy design that is mainly white-based with tinge of refreshing bright lime green.
- "New Age" simple and classy design that appeals to teenagers and young adults.
- Logo design to reinforce the vision of company.

Rough idea of what we have in mind but pls do not let this restrict your creativity:
- White and bright green base
- 2 sided print
- Front with simple information of Name and Designation as well as de-bossed/letterpressed print
- Details of on reverse side
- Contact details can be categorized as " find me" - address, "call me" - contact number , "email me" - email address, " Find out more"- website.

Information:

Name: Darel K Thuam
Title: Managing Director
Address: 41 Pelham Crescent, #07-15, Singapore 654321
Contact: +65 91234056
Email: darelthuam@mailvesta.com
Website: www.qnl-tutor.com

Thank you all in advance! Looking forward to some amazing designs from all you talented folks!
Updates

hi all,

have updated the projected to a guranteed status from the initial refundable status.

Thanks 

Dear designers,

I've included more info into the brief on design elements to include. 

Thanks for your participation and efforts!

Cheers!

Target Market(s)

young parents with school going children

Industry/Entity Type

Training

Requirements
Must have
• debossed/letterpressed logo
feel free to be creative with ur designs!
Nice to have
• round edges
Logo/name could have some elements of education/knowledge/path-to-learning incorporated in the design concept

```html
<!DOCTYPE html>
<html lang="en">
<head>
<meta charset="utf-8">
<title>The Quill and Lantern – Business Card</title>
<link href="https://fonts.googleapis.com/css2?family=Oswald:wght@400;500;600&display=swap" rel="stylesheet">
<style>
  :root {
    --lime: #b2c10f;
    --lime-deep: #9aab08;
    --paper: #f6f6f2;
    --backdrop: #e9e8e2;
    --edge: #d9d9d2;
  }
  * { box-sizing: border-box; margin: 0; padding: 0; }
  html, body {
    width: 1200px; height: 593px; overflow: hidden;
    background: var(--backdrop);
    font-family: "Oswald", "Arial Narrow", sans-serif;
  }
  .stage {
    width: 1200px; height: 593px;
    display: flex; align-items: center; justify-content: center; gap: 60px;
  }
  .card {
    width: 500px; height: 286px;
    border-radius: 18px;
    position: relative;
    box-shadow: 0 6px 18px rgba(0,0,0,0.12);
  }
  .card-front {
    background: var(--lime);
    display: flex; align-items: center; justify-content: center;
  }
  .front-name {
    color: #ffffff;
    font-weight: 600;
    font-size: 52px;
    line-height: 1.0;
    text-align: center;
    text-transform: uppercase;
    letter-spacing: 0.5px;
  }
  .card-back {
    background: var(--paper);
    border: 3px solid var(--lime);
    display: flex; align-items: center;
    padding: 0 30px 0 40px;
    color: var(--lime-deep);
  }
  .back-brand {
    width: 170px;
    text-align: right;
    font-weight: 600;
    font-size: 30px;
    line-height: 1.0;
    text-transform: uppercase;
    padding-right: 18px;
    align-self: flex-end;
    margin-bottom: 70px;
  }
  .divider {
    width: 1.5px; height: 180px;
    background: var(--lime);
  }
  .details {
    padding-left: 20px;
    text-transform: uppercase;
  }
  .holder-name {
    font-weight: 500; font-size: 20px; line-height: 1.1;
  }
  .holder-title {
    font-size: 10px; letter-spacing: 1.5px; margin-bottom: 10px;
  }
  .rule {
    width: 220px; height: 1.5px; background: var(--lime); margin: 0 0 12px -20px;
  }
  .contact-list { list-style: none; }
  .contact-item {
    display: flex; align-items: flex-start; gap: 10px;
    font-size: 10.5px; letter-spacing: 1px; line-height: 1.35;
    margin-bottom: 6px;
  }
  .contact-item .email, .contact-item .web { text-transform: uppercase; }
  .icon { width: 12px; height: 12px; flex: none; margin-top: 1px; fill: var(--lime-deep); }
</style>
</head>
<body>
<main class="stage">
  <section class="card card-front" aria-label="Card front">
    <h1 class="front-name">The Quill<br>and Lantern</h1>
  </section>

  <section class="card card-back" aria-label="Card back">
    <div class="back-brand">The Quill<br>and Lantern</div>
    <div class="divider"></div>
    <div class="details">
      <p class="holder-name">Darel K. Thuam</p>
      <p class="holder-title">Managing Director</p>
      <div class="rule"></div>
      <ul class="contact-list">
        <li class="contact-item">
          <svg class="icon" viewBox="0 0 12 12" aria-hidden="true"><path d="M6 1 L11.5 6 H10 V11 H7.5 V8 H4.5 V11 H2 V6 H0.5 Z"/></svg>
          <span>41 Pelham Crescent, #07-15,<br>Singapore 654321</span>
        </li>
        <li class="contact-item">
          <svg class="icon" viewBox="0 0 12 12" aria-hidden="true"><path d="M2.5 1 L4.5 1 L5.5 3.8 L4.2 4.8 C4.8 6.2 5.8 7.2 7.2 7.8 L8.2 6.5 L11 7.5 L11 9.5 C11 10.4 10.3 11 9.5 11 C5 11 1 7 1 2.5 C1 1.7 1.6 1 2.5 1 Z"/></svg>
          <span>+65 91234056</span>
        </li>
        <li class="contact-item">
          <svg class="icon" viewBox="0 0 12 12" aria-hidden="true"><path d="M0.5 2.5 H11.5 V9.5 H0.5 Z M1.5 3.2 L6 6.6 L10.5 3.2 Z" fill-rule="evenodd"/></svg>
          <span class="email">darelthuam@mailvesta.com</span>
        </li>
        <li class="contact-item">
          <svg class="icon" viewBox="0 0 12 12" aria-hidden="true"><path d="M1 1.5 H11 V8.5 H6.5 L4 11 V8.5 H1 Z"/></svg>
          <span class="web">www.qnl-tutor.com</span>
        </li>
      </ul>
    </div>
  </section>
</main>
</body>
</html>
```